Fitness competition business needs a card design

I need a professional business card design using my logo. The card will be horizontal with rounded edges.

Target Market(s)

Female fitness competitors

Industry/Entity Type

Fitness

Contact Information for Business Card

Rose-Lynn Darby
Owner
stagevarno.com
555.301.2187
info@stagevarno.com

Font styles to use
Serif

Colors

Designer to choose colors to be used in the design.

Requirements
Must have
• On the back please add the following:
• Figure
• Bikini
• Physique
• Fitness
Nice to have
• Looking for a very sleek design, contemporary and easy to read.
Should not have
• Should not be difficult to read or be too busy

```html
<!DOCTYPE html>
<html lang="en">
<head>
<meta charset="utf-8">
<title>Stage Varno – Business Card</title>
<link rel="stylesheet" href="https://fonts.googleapis.com/css2?family=Noto+Serif:ital,wght@0,400;0,700;1,700&display=swap">
<style>
  :root {
    --backdrop: #8a8f90;
    --card-black: #151515;
    --emboss: #232323;
    --emboss-edge: #0b0b0b;
    --card-white: #ffffff;
    --ink: #3a3a3a;
    --ink-soft: #4a4a4a;
    --accent-red: #e0202a;
    --serif: "Noto Serif", Georgia, serif;
  }
  * { box-sizing: border-box; margin: 0; padding: 0; }
  html, body { width: 1200px; height: 1000px; overflow: hidden; }
  body {
    background: var(--backdrop);
    font-family: var(--serif);
    position: relative;
  }
  .card {
    position: absolute;
    width: 500px;
    height: 290px;
    border-radius: 18px;
    box-shadow: 0 10px 24px rgba(0,0,0,.25);
  }
  /* Front side */
  .card--front {
    left: 350px;
    top: 160px;
    background: var(--card-black);
    display: flex;
    flex-direction: column;
    align-items: center;
    justify-content: center;
  }
  .front-brand {
    font-family: var(--serif);
    font-weight: 700;
    font-size: 52px;
    letter-spacing: 4px;
    text-transform: uppercase;
    color: var(--emboss);
  }
  .front-rule {
    width: 290px;
    height: 4px;
    margin-top: 12px;
    background: var(--emboss);
    box-shadow: 0 8px 0 var(--emboss);
  }
  /* Back side */
  .card--back {
    left: 350px;
    top: 530px;
    background: var(--card-white);
    overflow: hidden;
  }
  .back-lines { position: absolute; inset: 0; }
  .holder-name {
    position: absolute;
    right: 218px;
    top: 78px;
    font-style: italic;
    font-weight: 700;
    font-size: 25px;
    color: var(--ink);
    white-space: nowrap;
  }
  .holder-role {
    position: absolute;
    left: 306px;
    top: 70px;
    font-size: 17px;
    color: var(--ink-soft);
  }
  .contact {
    position: absolute;
    right: 218px;
    top: 128px;
    list-style: none;
    text-align: right;
    font-size: 16px;
    line-height: 24px;
    color: var(--ink-soft);
  }
  .divisions {
    position: absolute;
    left: 306px;
    top: 140px;
    list-style: none;
    font-size: 17px;
    line-height: 29px;
    color: var(--ink-soft);
  }
  .back-brand {
    position: absolute;
    left: 50px;
    bottom: 26px;
    font-weight: 700;
    font-size: 20px;
    letter-spacing: 1px;
    color: var(--ink);
  }
</style>
</head>
<body>
  <section class="card card--front" aria-label="Card front">
    <div class="front-brand">Stage Varno</div>
    <div class="front-rule"></div>
  </section>

  <section class="card card--back" aria-label="Card back">
    <svg class="back-lines" width="500" height="290" viewBox="0 0 500 290" aria-hidden="true">
      <line x1="290" y1="18" x2="290" y2="272" stroke="var(--accent-red)" stroke-width="2"/>
      <line x1="50" y1="114" x2="360" y2="114" stroke="var(--accent-red)" stroke-width="2"/>
    </svg>
    <div class="holder-name">Rose-Lynn Darby</div>
    <div class="holder-role">Owner</div>
    <ul class="contact">
      <li>stagevarno.com</li>
      <li>555.301.2187</li>
      <li>info@stagevarno.com</li>
    </ul>
    <ul class="divisions">
      <li>Figure</li>
      <li>Bikini</li>
      <li>Physique</li>
      <li>Fitness</li>
    </ul>
    <div class="back-brand">Stage Varno</div>
  </section>
</body>
</html>
```